Concierge Healthcare Business Card Design and Logo

We need a logo and business card design for a new company called "Sound Keeper". We will provide concierge audiological care, hearing aids, hearing exams, custom hearing protection etc to patients in the comfort of their homes and offices. We would like a sleek and modern design preferably with an Ear related logo.

Target Market(s)

People with hearing loss, Hunters, Musicians
My usual clientele are older individuals so usually 50+ years old

Industry/Entity Type

Health Care

Contact Information for Business Card

Clara Whitfield, AuD
Audiologist
512-418-2967
soundkeeper@mailvista.net
www.soundkeeperclinic.net

Logo Text

Sound Keeper

Number of Pages Required

3 page

```html
<!DOCTYPE html>
<html lang="en">
<head>
<meta charset="utf-8">
<title>Sound Keeper — Business Card</title>
<link rel="stylesheet" href="https://fonts.googleapis.com/css2?family=Open+Sans:wght@400;600;700&display=swap">
<style>
  :root {
    --backdrop: #4a4340;
    --card: #0c0c0c;
    --brand-blue: #1e9be0;
    --text-light: #e8e8e8;
    --text-muted: #cfcfcf;
    --silver: #c8c8c8;
  }
  * { box-sizing: border-box; margin: 0; padding: 0; }
  html, body { width: 1200px; height: 900px; overflow: hidden; }
  body {
    background: var(--backdrop);
    font-family: "Open Sans", Arial, sans-serif;
    position: relative;
  }
  .card {
    position: absolute;
    top: 300px;
    width: 520px;
    height: 298px;
    background: var(--card);
    border-radius: 3px;
    box-shadow: 0 10px 28px rgba(0,0,0,0.45);
  }
  .card--front { left: 60px; }
  .card--back { left: 620px; }

  .brand {
    position: absolute;
    display: flex;
    align-items: center;
    gap: 10px;
    font-weight: 700;
    letter-spacing: 0.5px;
    white-space: nowrap;
  }
  .brand__dot { border-radius: 50%; flex: none; }
  .card--front .brand { left: 34px; top: 132px; color: var(--brand-blue); font-size: 23px; }
  .card--front .brand__dot { width: 22px; height: 22px; background: var(--brand-blue); }
  .card--back .brand {
    left: 0; right: 0; top: 124px; justify-content: center;
    color: var(--silver); font-size: 32px;
  }
  .card--back .brand__dot { width: 30px; height: 30px; background: var(--silver); }

  .divider {
    position: absolute;
    left: 262px; top: 70px;
    width: 1px; height: 160px;
    background: var(--brand-blue);
  }
  .contact {
    position: absolute;
    left: 278px; top: 66px;
    color: var(--text-light);
    font-size: 13px;
    line-height: 17px;
  }
  .contact__name { color: var(--brand-blue); font-weight: 700; font-size: 16px; line-height: 20px; }
  .contact__role { color: var(--text-muted); }
  .contact__address { margin-top: 16px; color: var(--text-muted); }
  .contact__list { list-style: none; margin-top: 16px; }
  .contact__list li { display: flex; align-items: center; gap: 9px; height: 18px; }
  .contact__icon { width: 10px; height: 10px; flex: none; fill: var(--brand-blue); }
</style>
</head>
<body>
  <section class="card card--front" aria-label="Business card front">
    <div class="brand"><span class="brand__dot"></span>SOUND KEEPER</div>
    <div class="divider"></div>
    <div class="contact">
      <p class="contact__name">Clara Whitfield</p>
      <p class="contact__role">Managing Director</p>
      <p class="contact__address">12345, Address Goes Here<br>Country Name, 123456.</p>
      <ul class="contact__list">
        <li>
          <svg class="contact__icon" viewBox="0 0 10 10" aria-hidden="true"><path d="M2 0.5 L3.6 2.6 L2.7 3.6 Q3.8 5.8 6.4 7.3 L7.4 6.4 L9.5 8 L8.4 9.5 Q2.5 8.5 0.5 1.6 Z"/></svg>
          512-418-2967
        </li>
        <li>
          <svg class="contact__icon" viewBox="0 0 10 10" aria-hidden="true"><path d="M0 2 H10 V8.5 H0 Z M0.8 2.6 L5 5.6 L9.2 2.6" stroke="#0c0c0c" stroke-width="0.8"/></svg>
          soundkeeper@mailvista.net
        </li>
        <li>
          <svg class="contact__icon" viewBox="0 0 10 10" aria-hidden="true"><circle cx="5" cy="5" r="4.6"/><path d="M0.6 5 H9.4 M5 0.4 Q2.4 5 5 9.6 Q7.6 5 5 0.4" fill="none" stroke="#0c0c0c" stroke-width="0.7"/></svg>
          www.soundkeeperclinic.net
        </li>
      </ul>
    </div>
  </section>

  <section class="card card--back" aria-label="Business card back">
    <div class="brand"><span class="brand__dot"></span>SOUND KEEPER</div>
  </section>
</body>
</html>
```